Square Business Cards for Our Restaurant / Event Venue

We need square business cards designed for the management team of our event venue and restaurant. On one side of the card should be the the Harbor Lantern 7 logo and URL www.harborlantern7.example. On the other side should be the Ember Logo and URL www.emberhall7.example. All employee details should be on the side with Ember logo. There will be a total of 5 cards to be created with the design.

Clara Bennquist
clara@harborlantern7.example

main 555.418.3072
direct 555.730.2946

4831 West Orchard Lane SE
Washington, DC 90417

Industry/Entity Type

Business

```html
<!DOCTYPE html>
<html lang="en">
<head>
<meta charset="utf-8">
<title>Harbor Lantern 7 – Business Card</title>
<link rel="stylesheet" href="https://fonts.googleapis.com/css2?family=Questrial&display=swap">
<style>
  :root {
    --backdrop: #e9e6e2;
    --card-dark: #1b1b1c;
    --card-light: #ffffff;
    --ink-light: #ffffff;
    --ink-muted: #cfcfcf;
    --accent-red: #b92027;
    --shadow: rgba(0, 0, 0, 0.28);
  }
  * { margin: 0; padding: 0; box-sizing: border-box; }
  html, body {
    width: 1200px;
    height: 960px;
    overflow: hidden;
    background: var(--backdrop);
    font-family: "Questrial", "Helvetica Neue", Arial, sans-serif;
  }
  .canvas {
    position: relative;
    width: 1200px;
    height: 960px;
  }
  .card {
    position: absolute;
    top: 220px;
    width: 520px;
    height: 520px;
    box-shadow: 6px 8px 18px var(--shadow);
  }
  .card--contact { left: 68px; background: var(--card-dark); }
  .card--brand { left: 612px; background: var(--card-light); }

  .venue-name {
    position: absolute;
    left: 40px;
    top: 78px;
    display: flex;
    align-items: center;
    gap: 16px;
    color: var(--ink-light);
    font-size: 76px;
    line-height: 1;
  }
  .venue-name .marker {
    width: 22px;
    height: 22px;
    border-radius: 50%;
    background: var(--accent-red);
  }
  .venue-url {
    position: absolute;
    left: 42px;
    top: 176px;
    color: var(--ink-muted);
    font-size: 18px;
    line-height: 1;
  }

  .contact-list {
    position: absolute;
    left: 36px;
    top: 296px;
    list-style: none;
    color: var(--ink-light);
    font-size: 20.5px;
    line-height: 1;
  }
  .contact-list li {
    display: flex;
    align-items: flex-start;
    height: 41px;
  }
  .contact-list li.address { height: auto; }
  .contact-list .icon {
    width: 26px;
    height: 20px;
    margin-right: 7px;
    flex: none;
    fill: var(--accent-red);
  }
  .contact-list .address-lines span { display: block; }
  .contact-list .address-lines span + span { margin-top: 17px; }

  .person-name {
    position: absolute;
    left: 452px;
    top: 488px;
    transform: rotate(-90deg);
    transform-origin: 0 0;
    color: var(--ink-light);
    font-size: 41px;
    line-height: 1;
    white-space: nowrap;
  }

  .brand-block {
    position: absolute;
    inset: 0;
    display: flex;
    flex-direction: column;
    align-items: center;
    justify-content: center;
    gap: 18px;
  }
  .brand-block .brand-name {
    display: flex;
    align-items: center;
    gap: 14px;
    color: var(--accent-red);
    font-size: 44px;
    line-height: 1;
  }
  .brand-block .marker {
    width: 18px;
    height: 18px;
    border-radius: 50%;
    background: var(--accent-red);
  }
  .brand-block .brand-url {
    color: var(--accent-red);
    font-size: 18px;
    line-height: 1;
  }
</style>
</head>
<body>
<main class="canvas">

  <section class="card card--contact">
    <div class="venue-name"><span>Ember</span><span class="marker"></span></div>
    <div class="venue-url">www.emberhall7.example</div>

    <ul class="contact-list">
      <li>
        <svg class="icon" viewBox="0 0 26 20" aria-hidden="true"><path d="M1 3h24v15H1z"/><path d="M2 4l11 8 11-8" stroke="#1b1b1c" stroke-width="1.6" fill="none"/></svg>
        <span>clara@harborlantern7.example</span>
      </li>
      <li>
        <svg class="icon" viewBox="0 0 26 20" aria-hidden="true"><path d="M1 7c0-4 24-4 24 0v2h-6V6H7v3H1z"/><path d="M5 10h16l2 8H3z"/><circle cx="13" cy="14" r="2.3" fill="#1b1b1c"/></svg>
        <span>555.418.3072</span>
      </li>
      <li>
        <svg class="icon" viewBox="0 0 26 20" aria-hidden="true"><rect x="7" y="0" width="12" height="20" rx="2"/><rect x="9" y="3" width="8" height="12" fill="#1b1b1c"/></svg>
        <span>555.730.2946</span>
      </li>
      <li class="address">
        <svg class="icon" viewBox="0 0 26 20" aria-hidden="true"><path d="M13 0a7 7 0 0 1 7 7c0 5-7 13-7 13S6 12 6 7a7 7 0 0 1 7-7z"/><circle cx="13" cy="7" r="2.6" fill="#1b1b1c"/></svg>
        <span class="address-lines">
          <span>4831 West Orchard Lane SE</span>
          <span>Washington, DC 90417</span>
        </span>
      </li>
    </ul>

    <div class="person-name">Clara Bennquist</div>
  </section>

  <section class="card card--brand">
    <div class="brand-block">
      <div class="brand-name"><span class="marker"></span><span>Harbor Lantern 7</span></div>
      <div class="brand-url">www.harborlantern7.example</div>
    </div>
  </section>

</main>
</body>
</html>
```